VELDRA WEBSITE

need to create a new website for VELDRA ltd
the company deals with all aspects of safety products & safety wear
we need a simple website to show
ideas can be taken from following website whose products we shall distribute in kenya
www.kwt.co.uk
www.torvik.eu
www.brimontgearhouse.com
www.gardovasupply.co.za

we need following tabs
1) home - basic company information
2) products - broken down to following categories ie gloves, head protection, ear protection, mouth protection, foot protection
3) contacts

the company profile is a reputable company dealing with all aspects of safety, HSE (health and safety equipment), and PPE (personal protective equipment)

the website should have the torvik logo for which we are an authorized distributor.
the torvi industrial range writeup can be picked from their website

Dear Designers, i shall be able to choose a final design in 2 weeks, sorry i have not been able to finalise this due to a personal reason

Target Market(s)

the buyers are all types of industry who care for their employees safety

Industry/Entity Type

Industrial

Requirements
Must have
• clean look, fresh look, user freindly
Nice to have
• clear images, quick links etc

```html
<!DOCTYPE html>
<html lang="en">
<head>
<meta charset="utf-8">
<title>Veldra – Safety Products</title>
<link href="https://fonts.googleapis.com/css2?family=Open+Sans:wght@300;400;600;700&display=swap" rel="stylesheet">
<style>
:root{
  --slate:#243540;
  --slate-dark:#1c2a33;
  --gold:#e8b325;
  --gold-text:#d99e12;
  --ink:#1c1c1c;
  --text:#555;
  --muted:#8a8a8a;
  --line:#dcdcdc;
  --page:#f2f2f2;
}
*{margin:0;padding:0;box-sizing:border-box}
html,body{width:1020px;height:1200px;overflow:hidden}
body{font-family:'Open Sans',sans-serif;background:var(--page);position:relative;color:var(--text)}
.backdrop-top{position:absolute;left:0;top:0;width:1020px;height:120px;background:var(--slate)}
.backdrop-mid{position:absolute;left:0;top:120px;width:1020px;height:365px;background:var(--slate-dark)}
.page{position:absolute;left:84px;top:0;width:864px;height:1073px;background:#fff}
.abs{position:absolute}
/* header */
.brand{left:41px;top:20px;display:flex;align-items:center;gap:8px}
.brand-mark{width:22px;height:22px;background:var(--gold)}
.brand-name{font-size:30px;font-weight:700;color:var(--slate);letter-spacing:1px}
.brand-tag{left:41px;top:88px;font-size:8px;font-weight:700;color:var(--slate);letter-spacing:.5px;width:150px;line-height:10px}
.call{right:27px;top:64px;font-size:14px;color:#333;white-space:nowrap}
.phone{right:27px;top:81px;font-size:21px;color:#222;white-space:nowrap;line-height:28px}
.social{left:565px;top:86px;display:flex;gap:5px}
.social span{width:19px;height:19px;background:#4a78a8;border-radius:2px}
/* nav */
.nav{left:0;top:120px;width:864px;height:41px;background:linear-gradient(#f1c63f,#e2a918)}
.nav a{position:absolute;top:11px;font-size:15px;color:#fff;text-decoration:none}
.nav i{position:absolute;top:0;width:1px;height:41px;background:rgba(150,100,0,.35)}
/* hero */
.hero{left:0;top:161px;width:864px;height:324px;background:linear-gradient(180deg,#5f9ad4 0%,#a9cbeb 45%,#6c6a62 75%,#4c2f2a 100%)}
.caption{left:488px;top:156px;width:348px;height:89px;background:rgba(90,100,110,.78);border:1px solid rgba(255,255,255,.2);padding:17px 0 0 22px;color:#fff;white-space:nowrap;overflow:hidden}
.caption h2{font-weight:400;font-size:22px;line-height:28px;letter-spacing:-.2px}
.caption p{font-size:12px;line-height:16px;margin-top:7px}
.dots{left:404px;top:303px;display:flex;gap:6px}
.dots span{width:12px;height:12px;border-radius:50%;background:#333}
.dots span:first-child{background:#888}
/* welcome */
.welcome{left:21px;top:516px;width:570px}
.welcome h1{font-size:21px;font-weight:400;color:var(--ink);letter-spacing:.3px;line-height:28px}
.lead{font-size:13.5px;color:#666;margin-top:4px;line-height:20px}
.body-copy{font-size:10.8px;line-height:21px;color:#555;margin-top:2px;width:565px}
.rule{left:21px;top:657px;width:571px;border-top:1px dotted #bbb}
.section-title{left:22px;top:678px;font-size:20px;font-weight:400;color:var(--gold-text)}
/* products */
.grid{left:20px;top:713px;width:577px;display:grid;grid-template-columns:repeat(5,1fr);row-gap:10px}
.card{height:163px;border:1px solid #e4e4e4;text-align:center;padding-top:17px}
.card .thumb{width:64px;height:80px;margin:0 auto;border-radius:6px}
.card h3{font-size:12px;font-weight:400;color:var(--ink);margin-top:17px}
.card p{font-size:9px;color:var(--muted);line-height:13px;margin-top:2px}
/* side boxes */
.box{left:611px;width:239px;border:1px solid var(--line);border-radius:3px;background:#fff}
.news{top:509px;height:288px}
.box h2{font-size:18px;font-weight:400;color:var(--slate);padding:13px 0 0 22px}
.news-head{height:40px;background:linear-gradient(#fff,#f2f2f2);border-bottom:1px solid #e6e6e6}
.news-item{position:absolute;left:21px;display:flex;gap:9px}
.news-item .thumb{width:76px;height:57px}
.news-item h4{font-size:11px;font-weight:600;color:var(--ink);margin-top:1px}
.news-item p{font-size:9.5px;color:var(--muted);line-height:15px;margin-top:1px}
.contact{top:808px;height:234px}
.contact address{font-style:normal;font-size:11px;line-height:19.5px;color:#222;padding:8px 0 0 24px}
/* footer */
.foot-links{left:99px;top:1106px;font-size:12px;color:#444}
.foot-links span{margin:0 4px;color:#777}
.copy{left:100px;top:1131px;font-size:11px;color:#777}
.partners{left:595px;top:1104px;display:flex;align-items:center;gap:14px}
.partner{font-size:22px;color:#333;font-weight:600}
</style>
</head>
<body>
<div class="backdrop-top"></div>
<div class="backdrop-mid"></div>
<div class="page">
  <div class="abs brand"><span class="brand-mark"></span><span class="brand-name">VELDRA</span></div>
  <div class="abs brand-tag">SPECIALIZED PROTECTIVE &amp; INDUSTRIAL PRODUCTS</div>
  <div class="abs social"><span></span><span></span><span></span></div>
  <div class="abs call">CALL US NOW</div>
  <div class="abs phone">+ 254-700-555-018</div>

  <nav class="abs nav">
    <a style="left:38px">HOME</a><i style="left:96px"></i>
    <a style="left:114px">ABOUT US</a><i style="left:195px"></i>
    <a style="left:221px">PRODUCTS</a><i style="left:300px"></i>
    <a style="left:331px">PARTNERS</a>
    <a style="left:437px">CONTACT</a><i style="left:606px"></i><i style="left:700px"></i>
  </nav>

  <div class="abs hero" role="img" aria-label="Site workers in hard hats and high-visibility vests beside a crane">
    <div class="abs caption"><h2>We Deliver Safety Products</h2><p>"Tomorrow" - your reward for working safely today</p></div>
    <div class="abs dots"><span></span><span></span><span></span><span></span></div>
  </div>

  <section class="abs welcome">
    <h1>WELCOME TO VELDRA WEBSITE HOMEPAGE</h1>
    <p class="lead">Duis tincidunt lectus quis dui viverra vestibulum. Suspendisse vulputate aliquam dui.</p>
    <p class="body-copy">Nulla elementum dui ut augue. Aliquam vehicula mi at mauris. Maecenas placerat, nisl at consequat rhoncus, sem nunc gravida justo, quis eleifend arcu velit quis lacus. Morbi magna magna, tincidunt a, mattis non, imperdiet vitae, tellus. Sed odio est, auctor ac, sollicitudin in, consequat vitae, orci. Fusce id felis.</p>
  </section>
  <div class="abs rule"></div>
  <h2 class="abs section-title">OUR PRODUCTS</h2>

  <div class="abs grid">
    <div class="card"><div class="thumb" role="img" aria-label="Safety harness" style="background:linear-gradient(#f07a4a,#d84a2a)"></div><h3>PRODUCT NAME</h3><p>Morbi magna magna<br>tincidunt a mattis</p></div>
    <div class="card"><div class="thumb" role="img" aria-label="Welding helmet" style="background:linear-gradient(#555,#1a1a1a)"></div><h3>PRODUCT NAME</h3><p>Morbi magna magna<br>tincidunt a mattis</p></div>
    <div class="card"><div class="thumb" role="img" aria-label="Work glove" style="background:linear-gradient(#3b5fc0,#1d2f70)"></div><h3>PRODUCT NAME</h3><p>Morbi magna magna<br>tincidunt a mattis</p></div>
    <div class="card"><div class="thumb" role="img" aria-label="Safety goggles" style="background:linear-gradient(#c9d8e4,#8fa3b3)"></div><h3>PRODUCT NAME</h3><p>Morbi magna magna<br>tincidunt a mattis</p></div>
    <div class="card"><div class="thumb" role="img" aria-label="Gas detector" style="background:linear-gradient(#f5dc2a,#d8b410)"></div><h3>PRODUCT NAME</h3><p>Morbi magna magna<br>tincidunt a mattis</p></div>
    <div class="card"><div class="thumb" role="img" aria-label="High-visibility vest" style="background:linear-gradient(#ffa040,#f07010)"></div><h3>PRODUCT NAME</h3><p>Morbi magna magna<br>tincidunt a mattis</p></div>
    <div class="card"><div class="thumb" role="img" aria-label="Hi-vis jackets" style="background:linear-gradient(90deg,#c8e040,#f07a30)"></div><h3>PRODUCT NAME</h3><p>Morbi magna magna<br>tincidunt a mattis</p></div>
    <div class="card"><div class="thumb" role="img" aria-label="Leather gloves and hard hat" style="background:linear-gradient(#e8cf8a,#b8d830)"></div><h3>PRODUCT NAME</h3><p>Morbi magna magna<br>tincidunt a mattis</p></div>
    <div class="card"><div class="thumb" role="img" aria-label="Dust masks" style="background:linear-gradient(#f4f4f4,#d0d0d0)"></div><h3>PRODUCT NAME</h3><p>Morbi magna magna<br>tincidunt a mattis</p></div>
    <div class="card"><div class="thumb" role="img" aria-label="Traffic marker post" style="background:linear-gradient(#f3dc30,#c8a810);width:16px"></div><h3>PRODUCT NAME</h3><p>Morbi magna magna<br>tincidunt a mattis</p></div>
  </div>

  <aside class="abs box news">
    <div class="news-head"><h2>LATEST NEWS</h2></div>
    <div class="news-item" style="top:55px"><div class="thumb" role="img" aria-label="Warehouse worker" style="background:linear-gradient(#8a6a5a,#3a4a6a)"></div><div><h4>NEWS TITTLE HERE</h4><p>Suspendisse vulputate<br>aliquam dui Nulla elemen</p></div></div>
    <div class="news-item" style="top:128px"><div class="thumb" role="img" aria-label="Worker with equipment" style="background:linear-gradient(#6aa0d8,#3a3a3a)"></div><div><h4>NEWS TITTLE HERE</h4><p>Suspendisse vulputate<br>aliquam dui Nulla elemen</p></div></div>
    <div class="news-item" style="top:201px"><div class="thumb" role="img" aria-label="Worker in hard hat" style="background:linear-gradient(#b8c0c8,#e0803a)"></div><div><h4>NEWS TITTLE HERE</h4><p>Suspendisse vulputate<br>aliquam dui Nulla elemen</p></div></div>
  </aside>

  <aside class="abs box contact">
    <h2>CONTACT US</h2>
    <address>Veldra Limited<br>Cedar Business Park, No. 9<br>Main Kiranga Road<br>P.O. Box 40210-00100<br>NAIROBI - KENYA.<br>Tel : +254 739 555 014<br>: +254 700 555 018<br>Email: info@veldra.co.ke<br>www.veldra.co.ke</address>
  </aside>
</div>

<div class="abs foot-links">HOME<span>|</span>ABOUT US<span>|</span>PRODUCTS<span>|</span>PARTNERS<span>|</span>CONTACT</div>
<div class="abs copy">Copyright © 2013 Company Name.&nbsp; All right reserved</div>
<div class="abs partners">
  <span class="partner">MARLOWE</span>
  <span class="partner">KWT</span>
  <span class="partner">Torvik</span>
</div>
</body>
</html>
```